Design Tweak needed for a current site

Design on top of an existing quiz funnel

Ideally we would like to tweak what we have already built here (moving elements, styles, adding simple elements etc): http://offers.rateplumfinder.com/could-you-cut-your-auto-premium

The flow:
1) User lands on the quiz page
2) User answers X questions and moves through the flow
3) Calculating user results screen
4) User reaches a success screen, and is subsequently redirected

Keys to the design:
1) We need to emphasize the quiz title as that will drive engagement. In this case, this is a quiz to see if you might be eligible to save money on car insurance.

2) At the end of the quiz we need to make it very, very clear that the user is eligible for savings and that in order to complete the process they are being redirected to another page where they need to fill out a form. It is critical that the design communicates this very clearly... We can count down the time left until redirect and we can use any order of elements to make this point. I think our current design does a very bad job of this.

3) We want to have a "calculating" step so that it seems like the page is working in the background

Goals of the design:
1) Polished, high quality experience throughout
2) User is clearly prepared to be redirected to the conversion funnel/landing page at the end
3) User understands the value of completing the quiz

Target Market(s)

designers

Industry/Entity Type

Moving

Number of Pages Required

1 page

Font styles to use
Sans Serif

Colors

Designer to choose colors to be used in the design.

Requirements
Must have
• This quiz funnel is a template so while the current use case is for auto insurance, we would like a design that also would work in other contexts.
Should not have
• We don't want to materially change the core functionality of the quiz itself... redesigning any of the elements or interactions is encouraged though

```html
<!DOCTYPE html>
<html lang="en">
<head>
<meta charset="UTF-8">
<title>CoverLane – Quiz</title>
<link href="https://fonts.googleapis.com/css2?family=Montserrat:wght@500;600;800&family=Source+Sans+3:wght@600&display=swap" rel="stylesheet">
<style>
  :root {
    --green-dark: #54ad4c;
    --green-light: #6fc868;
    --ring: #3db878;
    --indigo: #434ea1;
    --indigo-bar: #4451a3;
    --ink: #111111;
    --white: #ffffff;
    --art-tone: #e6e8f4;
  }
  * { margin: 0; padding: 0; box-sizing: border-box; }
  html, body { width: 1200px; height: 675px; overflow: hidden; background: var(--white); }
  .quiz-screen { position: relative; width: 1200px; height: 675px; font-family: "Montserrat", sans-serif; }

  .site-header {
    position: absolute; left: 0; top: 0; width: 1200px; height: 105px;
    background: linear-gradient(100deg, var(--green-dark) 0%, var(--green-light) 60%, var(--green-dark) 100%);
  }
  .brand { position: absolute; left: 34px; top: 20px; display: flex; align-items: center; gap: 14px; }
  .brand-dot { width: 61px; height: 61px; border-radius: 50%; border: 7px solid var(--white); }
  .brand-name { font-family: "Montserrat", sans-serif; font-weight: 600; font-size: 50px; color: var(--white); letter-spacing: -0.5px; line-height: 1; }

  .quiz-question {
    position: absolute; left: 0; width: 1200px; top: 197px; padding-left: 50px; text-align: center;
    font-weight: 800; font-size: 34.5px; color: var(--indigo); letter-spacing: 1.4px;
  }

  .answer-option {
    position: absolute; top: 298px; width: 174px; height: 165px;
    border: 3px solid var(--ring); border-radius: 50%;
  }
  .answer-option.sedan { left: 330px; }
  .answer-option.suv { left: 525px; top: 297px; }
  .answer-option.truck { left: 720px; top: 297px; }
  .vehicle-art {
    position: absolute; left: 22px; top: 40px; width: 124px; height: 46px;
    border-radius: 10px; background: var(--art-tone);
  }
  .answer-label {
    position: absolute; left: 4px; width: 100%; top: 100px; text-align: center;
    font-family: "Source Sans 3", sans-serif; font-weight: 600; font-size: 31px;
    color: var(--indigo); letter-spacing: 1.5px;
  }

  .progress { position: absolute; left: 502px; top: 548px; width: 220px; }
  .progress-step { font-weight: 500; font-size: 15.5px; color: var(--ink); letter-spacing: 0.6px; }
  .progress-track {
    position: relative; margin-top: 6px; width: 218px; height: 15px;
    border-radius: 8px; background: var(--indigo-bar); overflow: hidden;
  }
  .progress-fill { position: absolute; left: 0; top: 0; width: 107px; height: 15px; background: var(--green-dark); border-radius: 8px 0 0 8px; }
  .progress-knob {
    position: absolute; left: 47px; top: 0; width: 62px; height: 15px;
    background: var(--green-dark); border: 1.5px solid var(--white); border-radius: 8px;
  }
  .progress-percent { margin-top: 8px; margin-left: 79px; font-weight: 500; font-size: 15.5px; color: var(--ink); letter-spacing: 0.6px; }
</style>
</head>
<body>
<main class="quiz-screen">
  <header class="site-header">
    <div class="brand">
      <span class="brand-dot"></span>
      <span class="brand-name">CoverLane</span>
    </div>
  </header>

  <h1 class="quiz-question">What kind of car do you drive?</h1>

  <div class="answer-option sedan">
    <div class="vehicle-art" role="img" aria-label="Line illustration of a sedan"></div>
    <span class="answer-label">sedan</span>
  </div>
  <div class="answer-option suv">
    <div class="vehicle-art" role="img" aria-label="Line illustration of an SUV"></div>
    <span class="answer-label">SUV</span>
  </div>
  <div class="answer-option truck">
    <div class="vehicle-art" role="img" aria-label="Line illustration of a tanker truck"></div>
    <span class="answer-label">truck</span>
  </div>

  <div class="progress">
    <p class="progress-step">Question 2 to 4</p>
    <div class="progress-track">
      <div class="progress-fill"></div>
      <div class="progress-knob"></div>
    </div>
    <p class="progress-percent">50% completed</p>
  </div>
</main>
</body>
</html>
```